Need Eye Catching For Sale By Owner Signs

In need of a Eye Catching For Sale By Owner Sign design. I plan on using the sign to market buildings and raw land that I own. The design should be able to scale to different rectangular dimensions for example a yard stake sign or a large 4' x 6' sign to be tacked to plywood. The design should have a dead space near the bottom that I can insert more detail information into at a later time.

The main tag line "For Sale By Owner" and the contact number "319-562-4097" needs to be easily be read from a distance.

```html
<!DOCTYPE html>
<html lang="en">
<head>
<meta charset="utf-8">
<title>For Sale By Owner – Yard Sign</title>
<link rel="stylesheet" href="https://fonts.googleapis.com/css2?family=Roboto:wght@400;500;700;900&display=swap">
<style>
  :root {
    --sign-blue: #2b5fb3;
    --sign-white: #ffffff;
    --ink-black: #111111;
    --backdrop: #eef0f3;
  }
  * { margin: 0; padding: 0; box-sizing: border-box; }
  html, body {
    width: 1200px;
    height: 1000px;
    overflow: hidden;
    background: var(--backdrop);
    font-family: "Roboto", Arial, sans-serif;
  }
  .canvas {
    position: relative;
    width: 1200px;
    height: 1000px;
  }
  .sign {
    position: absolute;
    left: 45px;
    top: 147px;
    width: 1110px;
    height: 705px;
    background: var(--sign-blue);
    border: 8px solid var(--sign-white);
    box-shadow: 0 2px 10px rgba(0,0,0,0.12);
  }
  .headline {
    position: absolute;
    left: 72px;
    top: 22px;
    display: flex;
    align-items: flex-start;
  }
  .headline-for {
    display: block;
    width: 96px;
    height: 200px;
    position: relative;
  }
  .headline-for span {
    position: absolute;
    left: 50%;
    top: 50%;
    transform: translate(-50%, -50%) rotate(-90deg);
    color: var(--sign-white);
    font-weight: 400;
    font-size: 92px;
    letter-spacing: 2px;
    line-height: 1;
  }
  .headline-sale {
    color: var(--sign-white);
    font-weight: 900;
    font-size: 292px;
    line-height: 0.78;
    letter-spacing: 2px;
    margin-left: 4px;
    margin-top: 12px;
  }
  .by-owner {
    position: absolute;
    left: 0;
    right: 0;
    top: 268px;
    text-align: center;
    padding-left: 70px;
    color: var(--sign-white);
    font-weight: 400;
    font-size: 100px;
    line-height: 1;
    letter-spacing: 3px;
  }
  .phone-bar {
    position: absolute;
    left: 37px;
    right: 37px;
    top: 378px;
    height: 140px;
    background: var(--sign-white);
    display: flex;
    align-items: center;
    justify-content: center;
  }
  .phone-number {
    color: var(--ink-black);
    font-weight: 700;
    font-size: 138px;
    line-height: 1;
    letter-spacing: 2px;
  }
  .detail-space {
    position: absolute;
    left: 37px;
    right: 37px;
    top: 530px;
    bottom: 20px;
  }
</style>
</head>
<body>
  <main class="canvas">
    <section class="sign" aria-label="For Sale By Owner sign">
      <h1 class="headline">
        <span class="headline-for"><span>FOR</span></span>
        <span class="headline-sale">SALE</span>
      </h1>
      <p class="by-owner">BY OWNER</p>
      <div class="phone-bar">
        <p class="phone-number">319-562-4097</p>
      </div>
      <div class="detail-space"></div>
    </section>
  </main>
</body>
</html>
```